Brisk Yard, LLC Web Design

I would like a web site design for a new lawn care business I am creating for my son. This is what it looks like now.

http://www.briskyardllc.example

Target Market(s)

Target customer is blue collar or middle class people who do not have time to do all of the grunt work around their home such as mowing the lawn, clearing snow etc. Or they need help moving or moving something such as mulch or wood. Shoot for an economical audience that may not have thought about having these tasks done for them.

Industry/Entity Type

Lawn Care

Colors
acd037
9bcb3c
cadf82
eaf2cf

Requirements
Must have
• I put in greens below. The colors that were available were not the best greens or the greens I would think about. The greens on the web site are more close.
Nice to have
• Will have a few more pictures of the logo guy on different machines. Will upload as soon as I get.

```html
<!DOCTYPE html>
<html lang="en">
<head>
<meta charset="utf-8">
<title>Brisk Yard, LLC</title>
<link href="https://fonts.googleapis.com/css2?family=Open+Sans:wght@400;600;700;800&display=swap" rel="stylesheet">
<style>
:root{
  --grass-deep:#245a0c;
  --grass-dark:#357a14;
  --grass:#5da825;
  --grass-light:#7cc23a;
  --green:#8cc43a;
  --green-strong:#6fae22;
  --green-soft:#cadf82;
  --green-pale:#eaf2cf;
  --ink:#333;
  --muted:#6a6a6a;
  --white:#fff;
}
*{margin:0;padding:0;box-sizing:border-box}
html,body{width:755px;height:1200px;overflow:hidden}
body{
  font-family:"Open Sans",Arial,sans-serif;color:var(--ink);position:relative;
  background:
    radial-gradient(ellipse 60% 45% at 50% 30%,rgba(140,200,70,.55) 0%,rgba(140,200,70,0) 100%),
    radial-gradient(ellipse 70% 50% at 50% 75%,rgba(120,190,60,.45) 0%,rgba(120,190,60,0) 100%),
    radial-gradient(ellipse at 50% 50%,var(--grass) 0%,var(--grass-dark) 60%,var(--grass-deep) 100%);
}
.lawn-bg{position:absolute;inset:0}
.page{position:absolute;left:96px;top:13px;width:564px;height:1152px;background:var(--white);box-shadow:0 0 16px rgba(0,0,0,.45)}

.header{position:absolute;left:0;top:0;width:100%;height:82px}
.phone{position:absolute;left:16px;top:30px;display:flex;align-items:center;gap:7px;font-size:17px;font-weight:600;color:#4a4a4a}
.phone-icon{width:20px;height:20px;background:var(--green);border-radius:4px;display:flex;align-items:center;justify-content:center}
.brand{position:absolute;left:282px;top:24px;transform:translateX(-50%);display:flex;align-items:center;gap:7px;font-size:22px;font-weight:800;color:var(--green-strong);white-space:nowrap}
.brand-dot{width:26px;height:26px;border-radius:50%;background:var(--green)}
.social{position:absolute;right:16px;top:35px;display:flex;gap:5px}
.social span{width:12px;height:12px;border-radius:50%;background:var(--green)}

.nav{position:absolute;left:0;top:82px;width:100%;height:20px;background:var(--green);display:flex;padding-left:62px}
.nav a{font-size:7.5px;font-weight:700;color:var(--white);text-decoration:none;padding:0 10px;line-height:20px}
.nav a.active{background:var(--green-strong)}

.hero{position:absolute;left:0;top:102px;width:100%;height:238px;
  background:linear-gradient(180deg,#a9cde6 0%,#d9e9f1 18%,#2f5a26 30%,#24491c 44%,#5b8a3a 52%,#c9473c 60%,#e8d06a 63%,#6fa82c 68%,#8bc23f 85%,#6ea52a 100%)}
.hero-title{position:absolute;left:290px;top:134px;font-size:15px;font-weight:600;color:var(--white);text-shadow:0 1px 3px rgba(0,0,0,.55)}
.hero-dots{position:absolute;left:260px;top:220px;display:flex;gap:5px}
.hero-dots span{width:4px;height:4px;border-radius:50%;background:rgba(255,255,255,.55)}
.hero-dots span:first-child{background:var(--white)}

.section-title{font-size:13px;font-weight:700;color:var(--ink);margin-bottom:7px}
.section-text{font-size:7.5px;line-height:1.6;color:var(--muted)}

.about{position:absolute;left:0;top:340px;width:100%;height:186px;background:var(--white)}
.about-photo{position:absolute;left:6px;top:28px;width:178px;height:138px;
  background:linear-gradient(160deg,#eef3e6 0%,#c9e24a 28%,#3f6a2a 52%,#dfe64c 70%,#9bb07a 100%)}
.about-body{position:absolute;left:206px;top:40px;width:330px}
.button{position:absolute;left:206px;top:154px;width:68px;height:16px;background:var(--green);color:var(--white);font-size:7px;font-weight:700;text-align:center;line-height:16px;text-decoration:none}

.lawn{position:absolute;left:0;top:526px;width:100%;height:200px;background:linear-gradient(90deg,var(--green-pale) 0%,var(--green-soft) 100%)}
.lawn-body{position:absolute;left:24px;top:50px;width:210px}
.lawn-photo{position:absolute;left:280px;top:0;width:284px;height:200px;
  background:linear-gradient(180deg,#e6eef2 0%,#eef1ee 22%,#b8b6ae 32%,#7a9a4a 48%,#a6cf5a 62%,#6ea42c 80%,#8cc43a 100%)}

.snow{position:absolute;left:0;top:726px;width:100%;height:172px;background:var(--white)}
.snow-photo{position:absolute;left:18px;top:18px;width:178px;height:124px;
  background:linear-gradient(180deg,#f4f4f4 0%,#e4e4e4 30%,#c8342a 45%,#a82820 62%,#d5d5d5 75%,#9a9a9a 100%)}
.snow-body{position:absolute;left:218px;top:46px;width:330px}

.yard{position:absolute;left:0;top:898px;width:100%;height:207px;
  background:linear-gradient(100deg,#2c6512 0%,#47861f 40%,#6aa83a 62%,#8a3a2a 78%,#3a3a36 100%)}
.yard-body{position:absolute;left:24px;top:44px;width:240px}
.yard .section-title,.yard .section-text{color:var(--white)}
.yard .section-text{text-shadow:0 1px 2px rgba(0,0,0,.4)}

.footer{position:absolute;left:0;top:1105px;width:100%;height:47px;background:var(--white);display:flex;justify-content:center;align-items:center;gap:16px}
.footer a{font-size:6.5px;font-weight:700;color:var(--green-strong);text-decoration:none}
</style>
</head>
<body>
<div class="lawn-bg" role="img" aria-label="Close-up photo of green grass behind the page"></div>
<div class="page">
  <header class="header">
    <div class="phone">
      <span class="phone-icon"><svg width="12" height="12" viewBox="0 0 24 24"><path fill="#fff" d="M6.6 10.8a15.1 15.1 0 0 0 6.6 6.6l2.2-2.2c.3-.3.7-.4 1-.2 1.1.4 2.3.6 3.6.6.6 0 1 .4 1 1V20c0 .6-.4 1-1 1A17 17 0 0 1 3 4c0-.6.4-1 1-1h3.5c.6 0 1 .4 1 1 0 1.3.2 2.5.6 3.6.1.3 0 .7-.2 1z"/></svg></span>
      555-014-2500
    </div>
    <div class="brand"><span class="brand-dot"></span>Brisk Yard, LLC</div>
    <div class="social"><span></span><span></span><span></span></div>
  </header>
  <nav class="nav">
    <a class="active" href="#">HOME</a><a href="#">LAWN CARE</a><a href="#">SNOW REMOVAL</a><a href="#">YARD CARE</a><a href="#">CONTACT US</a><a href="#">SCHEDULE</a>
  </nav>
  <section class="hero" role="img" aria-label="Photo of a mowed lawn with red flower beds, trees, a house and a push mower">
    <div class="hero-title">Professional Lawn Mowing</div>
    <div class="hero-dots"><span></span><span></span><span></span><span></span></div>
  </section>
  <section class="about">
    <div class="about-photo" role="img" aria-label="Photos of a worker in a bright safety vest using yard equipment"></div>
    <div class="about-body">
      <h2 class="section-title">About Owen Harlow</h2>
      <p class="section-text">Brisk Yard, LLC is the name of Owen Harlow's summer, winter and fall work. For the last ten years he has been helping people by cutting their lawns, trimming trees, clearing snow and moving mulch. Owen now runs Brisk Yard, LLC, a locally owned business based in Maple Ridge, giving prompt, fair and careful service to every client.</p>
    </div>
    <a class="button" href="#">CONTACT US</a>
  </section>
  <section class="lawn">
    <div class="lawn-body">
      <h2 class="section-title">Lawn Care</h2>
      <p class="section-text">Brisk Yard, LLC considers this the most important part of a lawn service. Every yard gets a clean cut and trimmed edges, and we haul away clippings so your lawn looks neat, from spring to the first frost.</p>
    </div>
    <div class="lawn-photo" role="img" aria-label="Photo of a large house with a striped, freshly mowed lawn"></div>
  </section>
  <section class="snow">
    <div class="snow-photo" role="img" aria-label="Photo of a red pickup truck with a snow plow blade"></div>
    <div class="snow-body">
      <h2 class="section-title">Snow Removal</h2>
      <p class="section-text">For parking lots with larger square footage, we will use our skid loader made for the job. This machine gives us the ability to push snow to the least used areas of your property, allowing more space for traffic. Snow plowing requires timely commitment.</p>
    </div>
  </section>
  <section class="yard" role="img" aria-label="Photo of green grass with a red lawn mower on the right">
    <div class="yard-body">
      <h2 class="section-title">Yard Care</h2>
      <p class="section-text">Whether your yard needs to be cleaned after a long winter or you need fresh mulch for the beds, we can help. We move wood, mulch and stone, rake leaves and clear brush so your weekends stay free for the things you enjoy.</p>
    </div>
  </section>
  <footer class="footer">
    <a href="#">HOME</a><a href="#">LAWN CARE</a><a href="#">SNOW REMOVAL</a><a href="#">YARD CARE</a><a href="#">CONTACT US</a><a href="#">SCHEDULE</a>
  </footer>
</div>
</body>
</html>
```